Brantley Water Taxi and Transport

Need to redesign our business cards to relay that we do freight logistics and water taxi service. We also work with gov. agencies doing environmental clean up, oil spill response, remote site construction and work with many of the air taxi and helicopter services on Kodiak Island. Out website is www.brantleywatertaxi-example.com to get a better idea of what we do.

Contact Information for Business Card

I have a previous business card but it just has the logo on the front, and a sunset picture on the back with the contact info. It does not relay what we do and what we can help with. I like a simple straight forward design over a busy one.

Colors
3176b5
0455a3
cfdfed

Requirements
Must have
• logo, email, website, phone number

```html
<!DOCTYPE html>
<html lang="en">
<head>
<meta charset="utf-8">
<title>Brantley Water Taxi &amp; Transport — Business Card</title>
<link rel="stylesheet" href="https://fonts.googleapis.com/css2?family=Bebas+Neue&family=Poppins:wght@400;600&display=swap">
<style>
  :root {
    --sky: #3ab4e6;
    --navy: #17468f;
    --sun: #f59c22;
    --paper: #ffffff;
    --backdrop: #e8e5df;
    --ink-light: #ffffff;
    --ink-muted: #f2f7fb;
  }
  * { margin: 0; padding: 0; box-sizing: border-box; }
  html, body { width: 900px; height: 1200px; overflow: hidden; }
  body {
    background: var(--backdrop);
    font-family: "Poppins", Arial, sans-serif;
    position: relative;
  }
  .card {
    position: absolute;
    left: 86px;
    width: 736px;
    height: 430px;
    background: var(--paper);
    border-radius: 24px;
    overflow: hidden;
    box-shadow: 0 6px 18px rgba(0,0,0,0.18);
  }
  .card--front { top: 136px; }
  .card--back { top: 633px; }

  /* brand lockup: one colour, one weight */
  .brand {
    position: absolute;
    display: flex;
    align-items: center;
    color: var(--navy);
    font-weight: 600;
  }
  .brand__dot {
    border-radius: 50%;
    background: var(--sun);
    flex: none;
  }
  .brand__text { line-height: 1; }
  .brand__name { display: block; text-transform: uppercase; letter-spacing: 1px; }
  .brand__tagline { display: block; }

  .card--front .brand { left: 76px; top: 82px; gap: 26px; }
  .card--front .brand__dot { width: 58px; height: 58px; }
  .card--front .brand__name { font-size: 66px; }
  .card--front .brand__tagline { font-size: 28px; margin-top: 6px; }

  .card--back .brand { left: 0; right: 0; top: 150px; justify-content: center; gap: 30px; }
  .card--back .brand__dot { width: 84px; height: 84px; }
  .card--back .brand__name { font-size: 78px; }
  .card--back .brand__tagline { font-size: 32px; margin-top: 8px; }

  /* contact band */
  .band {
    position: absolute;
    left: 0; top: 254px;
    width: 100%; height: 144px;
  }
  .band__accent {
    position: absolute; left: 0; top: 0;
    width: 26px; height: 100%;
    background: var(--sun);
  }
  .band__contacts {
    position: absolute; left: 318px; top: 0; right: 0; height: 100%;
    background: var(--navy);
  }
  .band__identity {
    position: absolute; left: 26px; top: 0;
    width: 306px; height: 100%;
    background: var(--sky);
    clip-path: polygon(0 0, 292px 0, 306px 50%, 292px 100%, 0 100%);
    text-align: center;
    color: var(--ink-light);
  }
  .person__name {
    font-family: "Bebas Neue", "Arial Narrow", sans-serif;
    font-size: 36px;
    letter-spacing: 0.5px;
    margin-top: 44px;
    margin-left: -26px;
    line-height: 1;
  }
  .person__role {
    font-size: 18px;
    margin-top: 6px;
    margin-left: -26px;
    color: var(--ink-muted);
  }
  .contact-list {
    list-style: none;
    position: absolute; left: 352px; top: 30px;
    color: var(--ink-light);
    font-size: 15px;
    white-space: nowrap;
  }
  .contact-list li {
    display: flex; align-items: center; gap: 12px;
    height: 29px;
  }
  .contact-list svg { width: 20px; height: 20px; flex: none; }
</style>
</head>
<body>

<section class="card card--front" aria-label="Business card front">
  <div class="brand">
    <span class="brand__dot"></span>
    <span class="brand__text">
      <span class="brand__name">Brantley</span>
      <span class="brand__tagline">Water Taxi &amp; Transport</span>
    </span>
  </div>

  <div class="band">
    <div class="band__accent"></div>
    <div class="band__contacts"></div>
    <div class="band__identity">
      <p class="person__name">Jordan Avery</p>
      <p class="person__role">Manager</p>
    </div>
    <ul class="contact-list">
      <li>
        <svg viewBox="0 0 24 24" aria-hidden="true"><path fill="#f59c22" d="M3 9c0-3 4-5 9-5s9 2 9 5v1.5h-4.5V8.5c-1.5-.6-7.5-.6-9 0v2H3zM6 12h12l2 7H4zm6 1.6a2.4 2.4 0 1 0 0 4.8 2.4 2.4 0 0 0 0-4.8z"/></svg>
        <span>907-555-0142</span>
      </li>
      <li>
        <svg viewBox="0 0 24 24" aria-hidden="true"><rect x="3" y="6" width="18" height="12" rx="1" fill="#f59c22"/><path d="M3 6.5l9 6.5 9-6.5" fill="none" stroke="#17468f" stroke-width="1.6"/></svg>
        <span>info@brantleywatertaxi-example.com</span>
      </li>
      <li>
        <svg viewBox="0 0 24 24" aria-hidden="true"><g fill="none" stroke="#f59c22" stroke-width="2"><circle cx="12" cy="12" r="9"/><ellipse cx="12" cy="12" rx="4" ry="9"/><path d="M3 12h18M5 7h14M5 17h14"/></g></svg>
        <span>www.brantleywatertaxi-example.com</span>
      </li>
    </ul>
  </div>
</section>

<section class="card card--back" aria-label="Business card back">
  <div class="brand">
    <span class="brand__dot"></span>
    <span class="brand__text">
      <span class="brand__name">Brantley</span>
      <span class="brand__tagline">Water Taxi &amp; Transport</span>
    </span>
  </div>
</section>

</body>
</html>
```